Velvet Lantern - listen to podcasts from around the world

http://randompodcasts.com/Velvet Lantern lets you listen to randomly selected podcasts from around the world. You can filter the podcasts by language. The power of randomness allows you to escape filter bubbles and echo chambers and discover issues and perspectives that you never knew existed. The current website offers basic functionality and is only a demo. Don't assume that anything in the current "design" should stay in place. The goal of the design should be to make it as easy as possible to understand what the app offers, to listen to new podcasts, and to skip to the next podcast. The service will be offered both as mobile apps and directly on the website. We expect that most users will be on mobile devices which is why we are focusing on the mobile/web app design.In addition to the current functionality, the app should also offer search (allowing the user to listen to podcasts that match given keywords), allow the user to easily subscribe to the current podcast and show the profile picture of the current podcast.

Target Market(s)

People interested in podcasts, all around the world

Colors

Designer to choose colors to be used in the design.

Requirements
Must have
• The main challenge is how to communicate the concept of the app to the user. Podcasts are randomly selected and the user just skips to the next one when he/she wants to. The ability to filter podcasts by language is important but no other filters are needed. The point is to use the power of random selection to explore new surprising content.
Nice to have
• The app/website is targeting a global audience. The less reliant the design is on written language, the better.

```html
<!DOCTYPE html>
<html lang="en">
<head>
<meta charset="utf-8">
<title>Velvet Lantern – podcasts from around the world</title>
<link href="https://fonts.googleapis.com/css2?family=Montserrat:wght@600;700&family=Open+Sans:wght@400;600;700&display=swap" rel="stylesheet">
<style>
:root{
  --red:#f44343;
  --pink:#f2576a;
  --pink-soft:#ff8b8b;
  --grad-start:#ff6b7e;
  --grad-end:#ffa08a;
  --ink:#1f1f24;
  --grey:#8d8d94;
  --line:#e6e6ea;
  --paper:#ffffff;
  --dark-a:#4a4646;
  --dark-b:#2a2524;
}
*{box-sizing:border-box;margin:0;padding:0}
html,body{width:1200px;height:720px;overflow:hidden;background:var(--paper)}
body{position:relative;font-family:"Open Sans",Arial,sans-serif;color:var(--ink)}
.blob{position:absolute;border-radius:50%;background:var(--red)}
.blob--top-left{left:-124px;top:-108px;width:456px;height:456px}
.blob--top-right{left:636px;top:36px;width:232px;height:232px}
.blob--bottom-mid{left:349px;top:514px;width:148px;height:148px}
.blob--bottom-right{left:828px;top:428px;width:424px;height:424px}
.glow{position:absolute;left:40px;top:110px;width:1120px;height:500px;border-radius:60px;background:rgba(255,255,255,.92);filter:blur(30px)}

.screen{position:absolute;top:136px;width:207px;height:448px;overflow:hidden;background:var(--paper);box-shadow:0 10px 30px rgba(240,80,80,.12)}
.screen--1{left:62px}.screen--2{left:278px}.screen--3{left:495px}.screen--4{left:712px}.screen--5{left:928px}
.screen--dark{color:#fff}
.backdrop{position:absolute;inset:0;background:radial-gradient(ellipse at 50% 70%,#5a4538 0%,var(--dark-a) 45%,var(--dark-b) 100%)}
.backdrop::after{content:"";position:absolute;inset:0;background:linear-gradient(180deg,rgba(60,60,60,.6) 0%,rgba(30,28,28,.2) 50%,rgba(30,28,28,.7) 100%)}

.status{position:absolute;top:10px;left:16px;right:14px;display:flex;justify-content:space-between;align-items:center;font-size:7px;font-weight:600}
.status svg{width:30px;height:7px}
.header{position:absolute;top:40px;left:0;width:100%;height:16px}
.header .menu,.header .search,.header .back{position:absolute;top:0;width:14px;height:14px}
.header .menu{left:16px}
.header .search{right:16px}
.header .back{left:18px;width:18px}
.brand{position:absolute;left:0;right:0;top:3px;text-align:center;font-family:"Montserrat",Arial,sans-serif;font-weight:700;font-size:6.6px;letter-spacing:.5px;text-transform:uppercase}
.brand--pink{color:var(--pink);font-weight:600}
.confirm{position:absolute;left:160px;top:-3px;width:30px;height:21px;border-radius:11px;background:linear-gradient(90deg,var(--grad-start),var(--grad-end));box-shadow:0 3px 8px rgba(244,80,90,.35);display:flex;align-items:center;justify-content:center}

.tagline{position:absolute;top:111px;left:0;width:100%;text-align:center;font-weight:700;font-size:10px;line-height:12px}
.brand-mark{position:absolute;left:0;top:200px;width:100%;text-align:center;font-family:"Montserrat",Arial,sans-serif;font-weight:700;font-size:9px;letter-spacing:.6px;text-transform:uppercase;color:rgba(255,255,255,.5)}
.shuffle-main{position:absolute;left:72px;top:256px;width:62px;height:34px;border-radius:17px;background:linear-gradient(90deg,var(--grad-start),var(--grad-end));display:flex;align-items:center;justify-content:center;box-shadow:0 4px 12px rgba(255,100,110,.4)}
.prefs-label{position:absolute;top:315px;left:0;width:100%;text-align:center;font-family:"Montserrat",Arial,sans-serif;font-weight:600;font-size:6.2px;letter-spacing:.4px;color:var(--pink-soft)}
.add{position:absolute;left:90px;width:28px;height:28px;border:1px solid #fff;border-radius:50%;display:flex;align-items:center;justify-content:center}
.add--low{top:337px}.add--chips{top:376px}
.chips{position:absolute;top:334px;left:20px;width:167px;display:flex;flex-wrap:wrap;justify-content:center;gap:4px 4px}
.chip{height:14px;padding:0 8px;border-radius:7px;background:#fff;color:var(--pink);font-size:6.8px;font-weight:600;line-height:14px}

.langs{position:absolute;top:92px;left:17px;width:172px;list-style:none}
.langs li{position:absolute;left:0;width:100%;font-size:7.8px;display:flex;justify-content:space-between;align-items:center}
.langs svg{width:9px;height:7px}

.episode{position:absolute;top:80px;left:10px;width:187px;text-align:center;font-weight:700;font-size:10px;line-height:12px}
.show{position:absolute;top:120px;left:0;width:100%;text-align:center;font-size:7.4px;color:var(--grey)}
.host{position:absolute;top:144px;left:0;width:100%;text-align:center;font-size:8.4px;font-weight:700}
.follow{position:absolute;top:160px;left:96px;width:16px;height:16px}
.art{position:absolute;border-radius:50%;box-shadow:0 6px 16px rgba(0,0,0,.15)}
.art--main{left:58px;top:192px;width:92px;height:92px}
.art--warm{background:radial-gradient(circle at 50% 40%,#f7a21c,#f49a0c 60%,#e08a05)}
.art--night{background:radial-gradient(circle at 45% 40%,#6a4a34,#2d2420 65%,#151212)}
.art--rose{background:radial-gradient(circle at 50% 50%,#f6d6d6,#e8b5b8)}
.art--edge-right{left:206px;top:192px;width:92px;height:92px}
.art--edge-left{left:-62px;top:192px;width:92px;height:92px}
.round-btn{position:absolute;width:34px;height:34px;border-radius:50%;background:linear-gradient(135deg,var(--grad-start),#ff8f93);display:flex;align-items:center;justify-content:center;box-shadow:0 4px 10px rgba(244,80,90,.35)}
.round-btn--next{left:157px;top:221px}
.round-btn--prev{left:16px;top:221px}
.time{position:absolute;top:317px;font-size:6.4px;color:#55555c}
.time--now{left:18px}.time--total{right:14px}
.track{position:absolute;top:320px;left:42px;width:122px;height:1.5px;background:var(--line)}
.track .played{position:absolute;left:0;top:0;height:100%;width:54px;background:var(--red)}
.track .knob{position:absolute;left:50px;top:-3px;width:7px;height:7px;border-radius:50%;background:var(--red)}
.ctrl{position:absolute;top:341px;width:26px;height:26px;border-radius:50%;background:#fff;box-shadow:0 3px 8px rgba(244,80,90,.18);display:flex;align-items:center;justify-content:center}
.ctrl--timer{left:63px}.ctrl--love{left:122px}
.ctrl--play{left:90px;top:340px;width:28px;height:28px;background:#f25a5a;box-shadow:0 4px 10px rgba(244,80,90,.4)}
</style>
</head>
<body>
<div class="blob blob--top-left"></div>
<div class="blob blob--top-right"></div>
<div class="blob blob--bottom-mid"></div>
<div class="blob blob--bottom-right"></div>
<div class="glow"></div>

<!-- Welcome screen -->
<section class="screen screen--1 screen--dark">
  <div class="backdrop" role="img" aria-label="Photo of a listener wearing headphones, seen from behind"></div>
  <div class="status"><span>9:41</span><svg viewBox="0 0 30 7" fill="#fff"><rect x="0" y="5" width="1.5" height="2"/><rect x="2.5" y="4" width="1.5" height="3"/><rect x="5" y="2.5" width="1.5" height="4.5"/><rect x="7.5" y="1" width="1.5" height="6"/><path d="M12 3a5 5 0 0 1 7 0l-1 1a3.5 3.5 0 0 0-5 0zM14 5a2 2 0 0 1 3 0l-1.5 1.5z"/><rect x="22" y="1.5" width="7" height="4" rx="1"/></svg></div>
  <header class="header">
    <svg class="menu" viewBox="0 0 14 14" stroke="#fff" stroke-width="1.4"><path d="M1 3h12M1 7h12M1 11h8"/></svg>
    <div class="brand">Velvet Lantern</div>
    <svg class="search" viewBox="0 0 14 14" fill="none" stroke="#fff" stroke-width="1.4"><circle cx="6" cy="6" r="4"/><path d="M9 9l4 4"/></svg>
  </header>
  <p class="tagline">Travel outside of your echo<br>chamber and filter bubble,<br>listen to podcasts from<br>around the world</p>
  <div class="brand-mark">Velvet Lantern</div>
  <div class="shuffle-main"><svg width="18" height="14" viewBox="0 0 18 14" fill="none" stroke="#fff" stroke-width="1.4"><path d="M1 3h3l8 8h4M1 11h3l2.5-2.5M10 5.5L12 3h4M14 1l2 2-2 2M14 9l2 2-2 2"/></svg></div>
  <div class="prefs-label">LANGUAGE PREFERENCES</div>
  <div class="add add--low"><svg width="10" height="10" viewBox="0 0 10 10" stroke="#fff" stroke-width="1.2"><path d="M5 1v8M1 5h8"/></svg></div>
</section>

<!-- Language preference -->
<section class="screen screen--2">
  <div class="status"><span>9:41</span><svg viewBox="0 0 30 7" fill="#111"><rect x="0" y="5" width="1.5" height="2"/><rect x="2.5" y="4" width="1.5" height="3"/><rect x="5" y="2.5" width="1.5" height="4.5"/><rect x="7.5" y="1" width="1.5" height="6"/><path d="M12 3a5 5 0 0 1 7 0l-1 1a3.5 3.5 0 0 0-5 0zM14 5a2 2 0 0 1 3 0l-1.5 1.5z"/><rect x="22" y="1.5" width="7" height="4" rx="1"/></svg></div>
  <header class="header">
    <svg class="back" viewBox="0 0 18 14" fill="none" stroke="#111" stroke-width="1.3"><path d="M17 7H2M7 2L2 7l5 5"/></svg>
    <div class="brand brand--pink" style="left:-20px">Language Preference</div>
    <div class="confirm"><svg width="14" height="9" viewBox="0 0 14 9" fill="none" stroke="#fff" stroke-width="1.2"><path d="M1 5l3 3 6-7M6 7l1 1 6-7"/></svg></div>
  </header>
  <ul class="langs">
    <li style="top:0">English US<svg viewBox="0 0 9 7" fill="none" stroke="#f25a5a" stroke-width="1.1"><path d="M1 3.5l2.5 2.5L8 1"/></svg></li>
    <li style="top:27px">English UK</li>
    <li style="top:56px">German<svg viewBox="0 0 9 7" fill="none" stroke="#f25a5a" stroke-width="1.1"><path d="M1 3.5l2.5 2.5L8 1"/></svg></li>
    <li style="top:85px">Frances<svg viewBox="0 0 9 7" fill="none" stroke="#f25a5a" stroke-width="1.1"><path d="M1 3.5l2.5 2.5L8 1"/></svg></li>
    <li style="top:113px">Russian</li>
    <li style="top:141px">Portugese</li>
    <li style="top:169px">Norwegian<svg viewBox="0 0 9 7" fill="none" stroke="#f25a5a" stroke-width="1.1"><path d="M1 3.5l2.5 2.5L8 1"/></svg></li>
  </ul>
</section>

<!-- Welcome with chosen languages -->
<section class="screen screen--3 screen--dark">
  <div class="backdrop" role="img" aria-label="Photo of a listener wearing headphones, seen from behind"></div>
  <div class="status"><span>9:41</span><svg viewBox="0 0 30 7" fill="#fff"><rect x="0" y="5" width="1.5" height="2"/><rect x="2.5" y="4" width="1.5" height="3"/><rect x="5" y="2.5" width="1.5" height="4.5"/><rect x="7.5" y="1" width="1.5" height="6"/><path d="M12 3a5 5 0 0 1 7 0l-1 1a3.5 3.5 0 0 0-5 0zM14 5a2 2 0 0 1 3 0l-1.5 1.5z"/><rect x="22" y="1.5" width="7" height="4" rx="1"/></svg></div>
  <header class="header">
    <svg class="menu" viewBox="0 0 14 14" stroke="#fff" stroke-width="1.4"><path d="M1 3h12M1 7h12M1 11h8"/></svg>
    <div class="brand">Velvet Lantern</div>
    <svg class="search" viewBox="0 0 14 14" fill="none" stroke="#fff" stroke-width="1.4"><circle cx="6" cy="6" r="4"/><path d="M9 9l4 4"/></svg>
  </header>
  <p class="tagline">Travel outside of your echo<br>chamber and filter bubble,<br>listen to podcasts from<br>around the world</p>
  <div class="brand-mark">Velvet Lantern</div>
  <div class="shuffle-main"><svg width="18" height="14" viewBox="0 0 18 14" fill="none" stroke="#fff" stroke-width="1.4"><path d="M1 3h3l8 8h4M1 11h3l2.5-2.5M10 5.5L12 3h4M14 1l2 2-2 2M14 9l2 2-2 2"/></svg></div>
  <div class="prefs-label">LANGUAGE PREFERENCES</div>
  <div class="chips"><span class="chip">English</span><span class="chip">German</span><span class="chip">French</span><span class="chip">Norwegian</span></div>
  <div class="add add--chips"><svg width="10" height="10" viewBox="0 0 10 10" stroke="#fff" stroke-width="1.2"><path d="M5 1v8M1 5h8"/></svg></div>
</section>

<!-- Player: first episode -->
<section class="screen screen--4">
  <div class="status"><span>9:41</span><svg viewBox="0 0 30 7" fill="#111"><rect x="0" y="5" width="1.5" height="2"/><rect x="2.5" y="4" width="1.5" height="3"/><rect x="5" y="2.5" width="1.5" height="4.5"/><rect x="7.5" y="1" width="1.5" height="6"/><path d="M12 3a5 5 0 0 1 7 0l-1 1a3.5 3.5 0 0 0-5 0zM14 5a2 2 0 0 1 3 0l-1.5 1.5z"/><rect x="22" y="1.5" width="7" height="4" rx="1"/></svg></div>
  <header class="header">
    <svg class="menu" viewBox="0 0 14 14" stroke="#111" stroke-width="1.4"><path d="M1 3h12M1 7h12M1 11h8"/></svg>
    <div class="brand brand--pink">Velvet Lantern</div>
    <svg class="search" viewBox="0 0 14 14" fill="none" stroke="#111" stroke-width="1.4"><circle cx="6" cy="6" r="4"/><path d="M9 9l4 4"/></svg>
  </header>
  <h2 class="episode">Tech Talk Roundtable 06-05<br>Gamifying Your Learning<br>with Nora Vale</h2>
  <p class="show">Northfield Learning Podcast</p>
  <p class="host">Rosa Delgado</p>
  <svg class="follow" viewBox="0 0 16 16" fill="none" stroke="#f25a5a" stroke-width="1.1"><circle cx="7" cy="5" r="3.2"/><path d="M1.5 15c0-3.5 2.5-5.5 5.5-5.5M11 10v5M8.5 12.5h5"/></svg>
  <div class="art art--main art--warm" role="img" aria-label="Podcast cover photo on an orange background"></div>
  <div class="art art--edge-right art--night" role="img" aria-label="Next podcast cover photo"></div>
  <div class="round-btn round-btn--next"><svg width="14" height="11" viewBox="0 0 18 14" fill="none" stroke="#fff" stroke-width="1.5"><path d="M1 3h3l8 8h4M1 11h3l2.5-2.5M10 5.5L12 3h4M14 1l2 2-2 2M14 9l2 2-2 2"/></svg></div>
  <span class="time time--now">27:06</span>
  <div class="track"><div class="played"></div><div class="knob"></div></div>
  <span class="time time--total">52:43</span>
  <div class="ctrl ctrl--timer"><svg width="11" height="11" viewBox="0 0 12 12" fill="none" stroke="#f25a5a" stroke-width="1.1"><circle cx="6" cy="7" r="4.3"/><path d="M6 7V4.5M4.5 1h3"/></svg></div>
  <div class="ctrl ctrl--play"><svg width="9" height="10" viewBox="0 0 9 10" fill="#fff"><path d="M1 0l8 5-8 5z"/></svg></div>
  <div class="ctrl ctrl--love"><svg width="11" height="10" viewBox="0 0 12 11" fill="none" stroke="#f25a5a" stroke-width="1.1"><path d="M6 10L1.6 5.6a2.6 2.6 0 0 1 4.4-3 2.6 2.6 0 0 1 4.4 3z"/></svg></div>
</section>

<!-- Player: next episode -->
<section class="screen screen--5">
  <div class="status"><span>9:41</span><svg viewBox="0 0 30 7" fill="#111"><rect x="0" y="5" width="1.5" height="2"/><rect x="2.5" y="4" width="1.5" height="3"/><rect x="5" y="2.5" width="1.5" height="4.5"/><rect x="7.5" y="1" width="1.5" height="6"/><path d="M12 3a5 5 0 0 1 7 0l-1 1a3.5 3.5 0 0 0-5 0zM14 5a2 2 0 0 1 3 0l-1.5 1.5z"/><rect x="22" y="1.5" width="7" height="4" rx="1"/></svg></div>
  <header class="header">
    <svg class="menu" viewBox="0 0 14 14" stroke="#111" stroke-width="1.4"><path d="M1 3h12M1 7h12M1 11h8"/></svg>
    <div class="brand brand--pink">Velvet Lantern</div>
    <svg class="search" viewBox="0 0 14 14" fill="none" stroke="#111" stroke-width="1.4"><circle cx="6" cy="6" r="4"/><path d="M9 9l4 4"/></svg>
  </header>
  <h2 class="episode">Living against your<br>greatest fears</h2>
  <p class="show">Quiet Hour Podcast</p>
  <p class="host">Theo Brandt</p>
  <svg class="follow" viewBox="0 0 16 16" fill="none" stroke="#f25a5a" stroke-width="1.1"><circle cx="7" cy="5" r="3.2"/><path d="M1.5 15c0-3.5 2.5-5.5 5.5-5.5M11 10v5M8.5 12.5h5"/></svg>
  <div class="art art--edge-left art--warm" role="img" aria-label="Previous podcast cover photo"></div>
  <div class="art art--main art--night" role="img" aria-label="Podcast host portrait photo"></div>
  <div class="art art--edge-right art--rose" role="img" aria-label="Next podcast cover photo"></div>
  <div class="round-btn round-btn--prev"><svg width="11" height="11" viewBox="0 0 11 11" fill="none" stroke="#fff" stroke-width="1.3"><path d="M2 1v9M10 1L3.5 5.5 10 10z"/></svg></div>
  <div class="round-btn round-btn--next"><svg width="14" height="11" viewBox="0 0 18 14" fill="none" stroke="#fff" stroke-width="1.5"><path d="M1 3h3l8 8h4M1 11h3l2.5-2.5M10 5.5L12 3h4M14 1l2 2-2 2M14 9l2 2-2 2"/></svg></div>
  <span class="time time--now">27:06</span>
  <div class="track"><div class="played"></div><div class="knob"></div></div>
  <span class="time time--total">52:43</span>
  <div class="ctrl ctrl--timer"><svg width="11" height="11" viewBox="0 0 12 12" fill="none" stroke="#f25a5a" stroke-width="1.1"><circle cx="6" cy="7" r="4.3"/><path d="M6 7V4.5M4.5 1h3"/></svg></div>
  <div class="ctrl ctrl--play"><svg width="9" height="10" viewBox="0 0 9 10" fill="#fff"><path d="M1 0l8 5-8 5z"/></svg></div>
  <div class="ctrl ctrl--love"><svg width="11" height="10" viewBox="0 0 12 11" fill="none" stroke="#f25a5a" stroke-width="1.1"><path d="M6 10L1.6 5.6a2.6 2.6 0 0 1 4.4-3 2.6 2.6 0 0 1 4.4 3z"/></svg></div>
</section>
</body>
</html>
```